Wine Bottle Label Logo Design

My fiancé and I are getting married in September and we made homemade wine which will be given to the guests as a wedding favor. We need label/logo for our wine bottles. We were looking for something rustic yet modern and simple. We had an idea for beige and cranberry colored wine stained, weathered, imperfect heart. Things that will need to be incorporated into the label design are as follows:
Our last name and also the name of the wine: Fusaldi
The year: 2012
Where is says Alcohol Content on a wine bottle normally write: Alcohol: Deceiving% by vol.
Type of wine: Red Wine
Incorporate our wedding date: Foot Stomped and Bottled for Nadia and Gus's Wedding Day 9/28/13
Wedding

```html
<!DOCTYPE html>
<html lang="en">
<head>
<meta charset="utf-8">
<title>Fusaldi Red Wine Label</title>
<link rel="stylesheet" href="https://fonts.googleapis.com/css2?family=Pinyon+Script&family=EB+Garamond:wght@400;500&display=swap">
<style>
  :root {
    --backdrop: #1c1b1c;
    --label-edge: #5e1816;
    --label-mid: #8a3a33;
    --label-center: #c9a48c;
    --gold: #efe0b0;
    --gold-deep: #b89548;
    --cranberry: #8e1512;
    --ink: #1e0f0c;
    --heart: #a8232a;
  }
  * { margin: 0; padding: 0; box-sizing: border-box; }
  html, body {
    width: 789px;
    height: 1200px;
    overflow: hidden;
    background: var(--backdrop);
  }
  .label {
    position: absolute;
    left: 44px;
    top: 100px;
    width: 700px;
    height: 1000px;
    border-radius: 22px;
    background:
      radial-gradient(ellipse 62% 48% at 50% 42%, var(--label-center) 0%, #b07f6b 40%, var(--label-mid) 75%, var(--label-edge) 100%);
    box-shadow: inset 0 0 40px rgba(40, 5, 5, 0.55);
    overflow: hidden;
    text-align: center;
  }
  .label__heart-ornament {
    position: absolute;
    left: 205px;
    top: 34px;
    width: 290px;
    height: 180px;
    border-radius: 50%;
    background: radial-gradient(ellipse at 50% 45%, var(--heart) 0%, #b0524a 40%, rgba(201, 164, 140, 0) 72%);
  }
  .label__cellar-scene {
    position: absolute;
    left: 170px;
    top: 230px;
    width: 360px;
    height: 360px;
    border-radius: 40% 40% 12px 12px;
    background: radial-gradient(ellipse at 50% 55%, rgba(110, 70, 55, 0.45) 0%, rgba(110, 70, 55, 0.18) 55%, rgba(110, 70, 55, 0) 80%);
  }
  .label__name {
    position: absolute;
    left: 0;
    right: 0;
    top: 230px;
    font-family: "Pinyon Script", cursive;
    font-size: 150px;
    line-height: 1;
    color: var(--gold);
    text-shadow: 2px 3px 3px rgba(60, 20, 10, 0.6);
  }
  .label__rings {
    position: absolute;
    left: 258px;
    top: 520px;
    width: 184px;
    height: 140px;
    border-radius: 50%;
    background: radial-gradient(ellipse at 50% 50%, var(--gold-deep) 0%, rgba(184, 149, 72, 0.55) 45%, rgba(184, 149, 72, 0) 75%);
  }
  .label__variety {
    position: absolute;
    left: 0;
    right: 0;
    top: 660px;
    font-family: "Pinyon Script", cursive;
    font-size: 70px;
    line-height: 1;
    color: var(--cranberry);
  }
  .label__vintage {
    position: absolute;
    left: 0;
    right: 0;
    top: 735px;
    font-family: "EB Garamond", serif;
    font-size: 64px;
    line-height: 1;
    color: var(--ink);
  }
  .label__details {
    position: absolute;
    left: 0;
    right: 0;
    top: 815px;
    font-family: "EB Garamond", serif;
    font-size: 25px;
    line-height: 35px;
    color: var(--ink);
  }
</style>
</head>
<body>
  <section class="label">
    <div class="label__heart-ornament" role="img" aria-label="Weathered cranberry heart with couple's monogram and flourishes"></div>
    <div class="label__cellar-scene" role="img" aria-label="Faint arched wine cellar illustration"></div>
    <h1 class="label__name">Fusaldi</h1>
    <div class="label__rings" role="img" aria-label="Two interlocking gold wedding rings"></div>
    <p class="label__variety">Red Wine</p>
    <p class="label__vintage">2012</p>
    <p class="label__details">
      Alcohol: Deceiving% by vol.<br>
      Foot Stomped and Bottled for<br>
      Nadia and Gus's Wedding Day 9/28/13
    </p>
  </section>
</body>
</html>
```